Project Report for American Indian and Alaska Native org (U.S.)

We need a report formatted/ design / layout.
We are a nonprofit organization that works on indigenous elder issues.
The report should reflect our logo color scheme.
Body font should be at least 11 point sans serif.
Ideally, headings and title would use fonts that are reminiscent of tribal cultures though not hard to read or whimsical/ unprofessional looking.

We have used some light script style fonts in the past -- nothing too cursive looking though.

The audience is public health professionals and tribal staff and leadership.

We want our organization's logo (QR7) and the project logo (brain health) incorporated into the title page.

We prefer the files to come back to us in an editable fashion + a pdf file.

Industry/Entity Type

tribal communities and public health officials

Font styles to use
Serif
Sans Serif

Requirements
Must have
• our logo and color scheme
Should not have
• headdress images

```html
<!DOCTYPE html>
<html lang="en">
<head>
<meta charset="utf-8">
<title>Tribal Law and Policy: Alzheimer's Disease and Related Dementia Issues</title>
<link rel="stylesheet" href="https://fonts.googleapis.com/css2?family=Merriweather:wght@900&family=Libre+Franklin:ital,wght@0,400;0,600;0,700;1,400&display=swap">
<style>
  :root {
    --backdrop: #f1f1f1;
    --page: #ffffff;
    --maroon: #6b2324;
    --brick: #b55c53;
    --teal: #5fa3a8;
    --ink-gray: #4a4a4a;
    --soft-gray: #9b9b9b;
    --mid-gray: #6a6a6a;
    --white: #ffffff;
  }
  * { margin: 0; padding: 0; box-sizing: border-box; }
  html, body {
    width: 1200px; height: 1200px; overflow: hidden;
    background: var(--backdrop);
  }
  .cover {
    position: absolute;
    left: 148px; top: 16px;
    width: 903px; height: 1168px;
    background: var(--page);
    overflow: hidden;
  }
  .pattern-strip {
    position: absolute;
    left: 751px; top: 143px;
    width: 107px; height: 1025px;
    background:
      linear-gradient(to bottom, rgba(255,255,255,1) 0%, rgba(255,255,255,0) 35%),
      linear-gradient(to right, var(--teal) 0%, #a88580 50%, var(--brick) 100%);
  }
  .eyebrow {
    position: absolute;
    left: 53px; top: 622px;
    font-family: "Libre Franklin", Arial, sans-serif;
    font-weight: 600;
    font-size: 23px;
    color: var(--ink-gray);
  }
  .report-title {
    position: absolute;
    left: 51px; top: 660px;
    font-family: "Merriweather", Georgia, serif;
    font-weight: 900;
    font-size: 57px;
    line-height: 66px;
    letter-spacing: -0.5px;
    color: var(--maroon);
    white-space: nowrap;
  }
  .report-date {
    position: absolute;
    left: 53px; top: 818px;
    font-family: "Libre Franklin", Arial, sans-serif;
    font-style: italic;
    font-size: 17px;
    color: var(--soft-gray);
  }
  .prepared-by {
    position: absolute;
    left: 53px; top: 840px;
    font-family: "Libre Franklin", Arial, sans-serif;
    font-size: 20px;
    color: var(--soft-gray);
  }
  .prepared-by strong { font-weight: 700; color: var(--mid-gray); }
  .prepared-by .for { font-size: 16px; }
  .org-band {
    position: absolute;
    left: 0; top: 868px;
    width: 751px; height: 161px;
    background: var(--brick);
    display: flex; align-items: center;
    padding-left: 53px;
    gap: 40px;
    font-family: "Libre Franklin", Arial, sans-serif;
    font-weight: 700;
    color: var(--white);
  }
  .org-mark { font-size: 78px; letter-spacing: -2px; line-height: 1; }
  .org-name { font-size: 33px; line-height: 40px; text-transform: uppercase; }
</style>
</head>
<body>
  <main class="cover">
    <p class="eyebrow">Tribal Law and Policy:</p>
    <h1 class="report-title">Alzheimer’s Disease and<br>Related Dementia Issues</h1>
    <p class="report-date">OCTOBER 27, 2021</p>
    <p class="prepared-by">PREPARED BY <strong>MARLOWE CONSULTING</strong> <span class="for">For</span></p>
    <section class="org-band">
      <span class="org-mark">QR7</span>
      <span class="org-name">Global Alliance for<br>Indigenous Elders</span>
    </section>
    <div class="pattern-strip" role="img" aria-label="Vertical zigzag pattern band fading from teal to brick red"></div>
  </main>
</body>
</html>
```